Business card for home developer

Name, email, phone #, logo, address, lic # and slogan.
Slogan to say something like, "Leader in quality neighborhood communities" maybe? The last one said "Leaders In Quality Living". Some thing saying we are above the other people.
The card can be two sided?
Home buyers
Business

```html
<!DOCTYPE html>
<html lang="en">
<head>
<meta charset="utf-8">
<title>Crestline Homes – Business Card</title>
<link rel="stylesheet" href="https://fonts.googleapis.com/css2?family=EB+Garamond:wght@400;500&display=swap">
<style>
  :root {
    --paper: #ffffff;
    --navy: #27457a;
    --ink: #3a3a3a;
    --rule: #b9c2d0;
    --divider: #1f1f1f;
  }
  * { box-sizing: border-box; margin: 0; padding: 0; }
  html, body { width: 1200px; height: 437px; overflow: hidden; background: var(--paper); }
  .card {
    position: relative;
    width: 1200px;
    height: 437px;
    background: var(--paper);
    font-family: "EB Garamond", Garamond, serif;
    color: var(--ink);
  }
  .brand {
    position: absolute;
    left: 100px;
    top: 150px;
    width: 460px;
    text-align: center;
  }
  .brand-name {
    display: inline-flex;
    align-items: center;
    gap: 12px;
    font-size: 40px;
    font-weight: 500;
    color: var(--navy);
    letter-spacing: 0.5px;
    line-height: 1;
  }
  .brand-dot {
    width: 14px;
    height: 14px;
    border-radius: 50%;
    background: var(--navy);
  }
  .brand-rule {
    width: 270px;
    height: 1px;
    margin: 16px auto 8px;
    background: var(--rule);
  }
  .slogan {
    font-size: 24px;
    letter-spacing: 0.5px;
    color: var(--ink);
  }
  .divider {
    position: absolute;
    left: 636px;
    top: 108px;
    width: 2px;
    height: 222px;
    background: linear-gradient(to bottom, rgba(31,31,31,0), var(--divider) 45%, var(--divider) 55%, rgba(31,31,31,0));
  }
  .contact {
    position: absolute;
    left: 736px;
    top: 130px;
    font-size: 21px;
    line-height: 1.25;
  }
  .contact-name {
    font-size: 30px;
    font-weight: 500;
    color: var(--navy);
    margin-bottom: 24px;
  }
  .contact-line { margin: 0; }
  .contact-list { margin-top: 8px; }
  .contact-item {
    display: flex;
    align-items: center;
    gap: 9px;
    margin-top: 2px;
  }
  .icon { width: 15px; height: 15px; fill: var(--navy); flex: none; }
</style>
</head>
<body>
  <main class="card">
    <section class="brand">
      <div class="brand-name"><span class="brand-dot"></span>Crestline Homes</div>
      <div class="brand-rule"></div>
      <p class="slogan">Leaders In Quality Living</p>
    </section>

    <div class="divider"></div>

    <section class="contact">
      <h1 class="contact-name">Name</h1>
      <p class="contact-line">Address Address</p>
      <p class="contact-line">Address Address Address</p>
      <div class="contact-list">
        <div class="contact-item">
          <svg class="icon" viewBox="0 0 16 16" aria-hidden="true">
            <rect x="3" y="0.5" width="10" height="15" rx="1.5"/>
            <rect x="5" y="2.5" width="6" height="5" fill="#fff"/>
            <rect x="5" y="9" width="1.6" height="1.4" fill="#fff"/>
            <rect x="7.2" y="9" width="1.6" height="1.4" fill="#fff"/>
            <rect x="9.4" y="9" width="1.6" height="1.4" fill="#fff"/>
            <rect x="5" y="11.4" width="1.6" height="1.4" fill="#fff"/>
            <rect x="7.2" y="11.4" width="1.6" height="1.4" fill="#fff"/>
            <rect x="9.4" y="11.4" width="1.6" height="1.4" fill="#fff"/>
          </svg>
          <span>D: 000 000 0000</span>
        </div>
        <div class="contact-item">
          <svg class="icon" viewBox="0 0 16 16" aria-hidden="true">
            <rect x="0.5" y="3" width="15" height="10.5" rx="1"/>
            <path d="M1.5 4 L8 9 L14.5 4" fill="none" stroke="#fff" stroke-width="1.2"/>
            <path d="M1.5 12.5 L6 8 M14.5 12.5 L10 8" fill="none" stroke="#fff" stroke-width="1"/>
          </svg>
          <span>email@email.com</span>
        </div>
      </div>
    </section>
  </main>
</body>
</html>
```